Web tool bar Project

I'm open to paying more if the quality of the bar is very good... if you feel the scope of the project does not match budget..... please quote me.

I need someone to re-design my web tool bar.

In the first attachment you can see a black tool bar (fig1). This is my old design. I want this to be the template as it shows what the text will say and where the buttons will be placed.

For the new tool bar:
-I would like the it to be white in colour (like fig.2)
-I would like the buttons to also be white. But the buttons must stand out so the designer should use the right shading to make the buttons stand out.
-The bar needs to be the quality of the bar in fig.2 (very good quality). I have had many designs done for this but no designer seems to be good enough to get the right quality.
-The text in the white boxes on the new bar should be the colours shown above the buttons next to fig.1 (blue, green, red, yellow, purple & orange).

Finally please put the logo attached (QT) at the end of the bar on the right where it says logo. The logo should blend in well with the bar as it has white in it also.

Please take note of fig.2 it is good quality with sharp edges I would like the same quality.

Any further questions please ask?

Requirements
Must have
• Quality!

```html
<!DOCTYPE html>
<html lang="en">
<head>
<meta charset="utf-8">
<title>QT Toolbar</title>
<link href="https://fonts.googleapis.com/css2?family=Signika:wght@600&display=swap" rel="stylesheet">
<style>
  :root {
    --page: #ffffff;
    --bar-top: #f1f1f1;
    --bar-bottom: #cfcfcf;
    --bar-edge: #9a9a9a;
    --btn-top: #fbfbfb;
    --btn-bottom: #e6e6e6;
    --btn-border: #a9a9a9;
    --green: #6aa322;
    --red: #b8321f;
    --yellow: #f0b400;
    --purple: #8f3b9e;
    --orange: #ef7418;
    --brand: #1e8fd6;
  }
  * { box-sizing: border-box; margin: 0; padding: 0; }
  html, body {
    width: 1200px; height: 132px; overflow: hidden;
    background: var(--page);
    font-family: "Signika", "Trebuchet MS", sans-serif;
  }
  .toolbar {
    position: absolute; left: 0; top: 70px;
    width: 1200px; height: 62px;
    background: linear-gradient(to bottom, var(--bar-top), var(--bar-bottom));
    border-top: 2px solid var(--bar-edge);
    box-shadow: 0 -1px 3px rgba(0,0,0,0.25);
  }
  .tool-button {
    position: absolute; top: 13px; height: 40px;
    display: flex; align-items: center; justify-content: center; gap: 6px;
    background: linear-gradient(to bottom, var(--btn-top), var(--btn-bottom));
    border: 1px solid var(--btn-border);
    border-radius: 3px;
    box-shadow: inset 0 1px 0 #ffffff, 0 1px 1px rgba(0,0,0,0.12);
    font-size: 12.5px; font-weight: 600; white-space: nowrap;
  }
  .tool-button svg { width: 14px; height: 14px; flex: none; }
  .check-in   { left: 496px; width: 89px;  color: var(--green); }
  .friends    { left: 592px; width: 198px; color: var(--red); }
  .feeds      { left: 797px; width: 123px; color: var(--yellow); }
  .messages   { left: 926px; width: 104px; color: var(--purple); }
  .scrapbook  { left: 1036px; width: 104px; color: var(--orange); }
  .brand {
    position: absolute; left: 1150px; top: 14px;
    width: 42px; height: 40px;
    display: flex; align-items: center; justify-content: center;
    color: var(--brand); font-size: 20px; font-weight: 600;
  }
</style>
</head>
<body>
  <nav class="toolbar">
    <div class="tool-button check-in">
      <svg viewBox="0 0 14 14" aria-hidden="true"><path d="M7 1a4 4 0 0 0-4 4c0 3 4 8 4 8s4-5 4-8a4 4 0 0 0-4-4z" fill="currentColor"/><circle cx="7" cy="5" r="1.5" fill="#fff"/></svg>
      Check In
    </div>
    <div class="tool-button friends">
      <svg viewBox="0 0 16 14" aria-hidden="true" style="width:16px"><circle cx="5" cy="4" r="2.6" fill="currentColor"/><path d="M0 13c0-3 2-5 5-5s5 2 5 5z" fill="currentColor"/><circle cx="11" cy="4.5" r="2.2" fill="currentColor"/><path d="M10 8.5c3 0 5 1.5 5.5 4.5H11c0-2-0.4-3.3-1-4.5z" fill="currentColor"/></svg>
      Online Friends at Circlehub
    </div>
    <div class="tool-button feeds">
      <svg viewBox="0 0 14 14" aria-hidden="true"><circle cx="2.5" cy="11.5" r="1.8" fill="currentColor"/><path d="M1 6a7 7 0 0 1 7 7" stroke="currentColor" stroke-width="2" fill="none"/><path d="M1 1.5a11.5 11.5 0 0 1 11.5 11.5" stroke="currentColor" stroke-width="2" fill="none"/></svg>
      Lounge Feeds
    </div>
    <div class="tool-button messages">
      <svg viewBox="0 0 14 14" aria-hidden="true"><ellipse cx="7" cy="6" rx="6.5" ry="4.8" fill="currentColor"/><path d="M3 9.5 1.5 13.5 6 10.5z" fill="currentColor"/></svg>
      Messages
    </div>
    <div class="tool-button scrapbook">
      <svg viewBox="0 0 14 14" aria-hidden="true"><path d="M1 3.5 7 5.5 13 3.5v8l-6 2-6-2z" fill="none" stroke="currentColor" stroke-width="1.3" stroke-linejoin="round"/><path d="M7 5.5v8" stroke="currentColor" stroke-width="1.3"/><path d="M3 2l4 1.5" stroke="currentColor" stroke-width="1.3"/></svg>
      Scrapbook
    </div>
    <div class="brand">QT</div>
  </nav>
</body>
</html>
```